Website for an electrical contractor :)

We are after a web site which can show pictures of our jobs and our capability in a professional, creative and easily understood way.

----- Bramwell Electrical ------

We really want a visually good looking website with three sections

Section one:
'Completed projects'
We have a few pictures of jobs which we've completed and would like to show off with a brief description. (see uploads)

Section two:
'Our capabilities'
Just a list of what services we offer

Section three:
We would like a 'contact us' section which people can send us a short msg and upload a file for plans to be able to send to us. We would need their name, phone number and email details. We would also need a short privacy policy saying 'we do not disclose information to third parties'.
We also want to display our contact number and postal address

Good luck :)

Target Market(s)

Adults 25 years+
Business owners
Builders
Real estate agents

Industry/Entity Type

Electrical

Colors

Designer to choose colors to be used in the design.

Requirements
Must have
• Visually appealing
Easy to understand
In the 'Completed projects' section, must have a list for each project we do i can upload pictures for it.

```html
<!DOCTYPE html>
<html lang="en">
<head>
<meta charset="utf-8">
<title>Bramwell Electrical</title>
<link href="https://fonts.googleapis.com/css2?family=Oswald:wght@400;600;700&family=Open+Sans:wght@400;600;800&display=swap" rel="stylesheet">
<style>
:root{
  --red:#e21b22;
  --red-deep:#c8141b;
  --ink:#111;
  --charcoal:#2b2826;
  --night:#141414;
  --white:#fff;
  --muted:#cfcfcf;
  --grey:#8d8d8d;
  --head:'Oswald',sans-serif;
  --body:'Open Sans',sans-serif;
}
*{box-sizing:border-box;margin:0;padding:0}
html,body{width:1200px;height:900px;overflow:hidden;background:#fff;font-family:var(--body)}
.canvas{position:relative;width:1200px;height:900px}
.abs{position:absolute}
.column{position:absolute;top:0;height:900px;overflow:hidden}
.column-left{left:0;width:576px;background:var(--charcoal)}
.column-right{left:577px;width:623px;background:var(--night)}

/* header */
.site-header{position:absolute;left:0;top:0;width:576px;height:48px;background:var(--white)}
.brand{position:absolute;left:44px;top:12px;display:flex;align-items:center;gap:5px}
.brand-mark{width:9px;height:9px;background:var(--red)}
.brand-name{font-family:var(--body);font-size:17px;color:#555;line-height:1}
.brand-tag{position:absolute;left:58px;top:31px;font-size:4px;color:#777;white-space:nowrap}
.main-nav{position:absolute;left:176px;top:13px;display:flex;gap:0;font-family:var(--head);font-size:8px;color:#555;text-transform:uppercase}
.main-nav a{color:inherit;text-decoration:none;height:24px;line-height:24px}
.nav-home{background:var(--red);color:#fff!important;border-radius:12px;width:46px;text-align:center;margin-right:10px}
.nav-link-2{margin-right:26px}.nav-link-3{margin-right:25px}.nav-link-4{margin-right:26px}

/* hero */
.hero{position:absolute;left:0;top:48px;width:576px;height:332px;background:linear-gradient(180deg,#5c6b80 0%,#7a8593 35%,#3b3e43 60%,#4a4a4a 100%)}
.hero-title{position:absolute;left:0;width:576px;top:96px;text-align:center;font-weight:800;font-size:29px;color:var(--red);letter-spacing:.3px}
.hero-sub{position:absolute;left:0;width:576px;top:133px;text-align:center;font-size:12.5px;color:#eee;letter-spacing:1.2px}
.btn-read{position:absolute;left:206px;top:166px;width:76px;height:24px;background:var(--red);color:#fff;font-size:8px;line-height:24px;text-align:center;text-transform:uppercase}
.btn-more{position:absolute;left:300px;top:166px;height:24px;line-height:24px;color:#fff;font-size:8px;text-transform:uppercase}
.hero-progress{position:absolute;left:0;top:329px;width:270px;height:3px;background:var(--red)}

/* projects */
.projects{position:absolute;left:0;top:380px;width:576px;height:440px;background:radial-gradient(ellipse at 50% 45%,#4a4542 0%,#2f2b29 60%,#201d1c 100%)}
.section-title{font-family:var(--head);font-weight:600;font-size:23px;color:#fff;text-transform:uppercase;text-align:center}
.section-title em{font-style:normal;color:var(--red)}
.section-lede{font-size:7.5px;color:#ddd;text-align:center}
.project-label{position:absolute;font-size:7.5px;color:#ddd;white-space:nowrap}
.feature-photo{position:absolute;left:182px;top:113px;width:204px;height:131px;border:3px solid #777;background:linear-gradient(180deg,#3a3936 0%,#9a9890 45%,#b8b4aa 100%)}
.feature-name{position:absolute;left:182px;top:253px;width:204px;text-align:center;font-family:var(--head);font-weight:600;font-size:11px;color:#fff;text-transform:uppercase}
.feature-text{position:absolute;left:182px;top:273px;width:204px;text-align:center;font-size:6.5px;line-height:1.45;color:#ddd}

.capabilities-peek{position:absolute;left:0;top:820px;width:576px;height:80px;background:#171717}

/* capabilities */
.capabilities{position:absolute;left:0;top:0;width:623px;height:408px;background:linear-gradient(160deg,#2a2a2a 0%,#151515 55%,#251819 100%)}
.cap-label{position:absolute;width:120px;text-align:center;font-size:11px;color:#eee}

/* contact */
.contact{position:absolute;left:0;top:408px;width:623px;height:447px;background:linear-gradient(180deg,#e3262b 0%,#d91a20 100%)}
.world-map{position:absolute;left:20px;top:50px;width:590px;height:330px;background:radial-gradient(ellipse at 50% 50%,rgba(255,255,255,.09),rgba(255,255,255,0) 70%)}
.field{position:absolute;left:159px;width:307px;border:1px solid rgba(255,255,255,.55);color:#fbe3e3;font-size:11px;padding-left:13px}
.field-line{height:34px;line-height:34px}
.field-area{height:113px;padding-top:10px;font-size:12.5px}
.btn-browse{position:absolute;left:316px;top:387px;width:70px;height:32px;background:#1b1b1b;color:#fff;font-size:13px;line-height:32px;text-align:center}
.btn-send{position:absolute;left:392px;top:387px;width:70px;height:32px;background:#b51017;color:#fff;font-size:13px;line-height:32px;text-align:center}

.site-footer{position:absolute;left:0;top:855px;width:623px;height:45px;background:#1a1a1a}
.copyright{position:absolute;left:46px;top:16px;font-size:9px;color:#bbb}
.social{position:absolute;top:11px;width:22px;height:22px;border:1.5px solid #ddd;border-radius:50%}

.dots{position:absolute;display:flex;flex-direction:column;gap:5px}
.dots span{width:5px;height:5px;border-radius:50%;background:#fff}
.dots .on{width:7px;height:7px;margin-left:-1px;background:var(--red)}
.dots .dark{background:#222}
</style>
</head>
<body>
<div class="canvas">

  <!-- left column -->
  <div class="column column-left">
    <header class="site-header">
      <div class="brand"><span class="brand-mark"></span><span class="brand-name">Bramwell</span></div>
      <div class="brand-tag">Electrical &amp; Communications Pty</div>
      <nav class="main-nav">
        <a class="nav-home">Home</a>
        <a class="nav-link-2">The Link to Asia Model</a>
        <a class="nav-link-3">Sample Programs</a>
        <a class="nav-link-4">Global Network</a>
        <a>Contact Us</a>
      </nav>
    </header>

    <section class="hero">
      <div class="abs" role="img" aria-label="Photo of a modern industrial building under a cloudy sky" style="inset:0;background:rgba(0,0,0,.15)"></div>
      <h1 class="hero-title">WELCOME TO BRAMWELL</h1>
      <p class="hero-sub">ELECTRICAL &amp; COMMUNICATIONS</p>
      <span class="btn-read">Read More</span>
      <span class="btn-more">More Details</span>
      <svg class="abs" style="left:0;top:0" width="576" height="332">
        <circle cx="275" cy="208" r="3" fill="#e21b22"/><circle cx="284" cy="208" r="3" fill="#fff"/><circle cx="293" cy="208" r="3" fill="#fff"/>
        <rect x="281" y="285" width="14" height="23" rx="7" fill="none" stroke="#ddd" stroke-width="1.3"/>
        <line x1="288" y1="290" x2="288" y2="296" stroke="#ddd" stroke-width="1.3"/>
      </svg>
      <div class="dots" style="left:546px;top:160px"><span class="on"></span><span></span><span></span><span></span><span></span></div>
      <div class="hero-progress"></div>
    </section>

    <section class="projects">
      <h2 class="section-title abs" style="left:0;width:576px;top:26px"><em>Completed</em> Projects</h2>
      <p class="section-lede abs" style="left:0;width:576px;top:62px">We have a few pictures of jobs which we've completed and would like to show off with a brief description</p>

      <svg class="abs" style="left:0;top:0" width="576" height="440" aria-hidden="true">
        <g fill="none" stroke="#bbb" stroke-width="1" stroke-dasharray="4 3">
          <polyline points="120,104 120,98 452,98 452,104"/>
          <polyline points="93,132 78,132 78,165 93,165"/>
          <polyline points="93,198 78,198 78,265 93,265"/>
          <polyline points="93,298 78,298 78,330 120,330 120,302"/>
          <polyline points="479,132 494,132 494,165 479,165"/>
          <polyline points="479,198 494,198 494,262 479,262"/>
          <polyline points="147,330 259,330"/>
          <polyline points="313,330 425,330"/>
        </g>
        <g stroke="#fff" stroke-width="2">
          <polygon points="120,104 147,131 120,158 93,131" fill="#6d6660"/>
          <polygon points="120,164 147,191 120,218 93,191" fill="#3d4c5a"/>
          <polygon points="120,238 147,265 120,292 93,265" fill="#a29f97"/>
          <polygon points="120,302 147,329 120,356 93,329" fill="#7a6a58"/>
          <polygon points="452,104 479,131 452,158 425,131" fill="#8a8c90"/>
          <polygon points="452,164 479,191 452,218 425,191" fill="#6f8fb0"/>
          <polygon points="452,236 479,262 452,289 425,262" fill="#7b7a78"/>
          <polygon points="452,302 479,329 452,356 425,329" fill="#5f6f60"/>
          <polygon points="286,303 313,330 286,357 259,330" fill="#6f8aa6"/>
        </g>
        <rect x="281" y="396" width="14" height="23" rx="7" fill="none" stroke="#ddd" stroke-width="1.3"/>
        <line x1="288" y1="401" x2="288" y2="407" stroke="#ddd" stroke-width="1.3"/>
      </svg>
      <span class="abs" role="img" aria-label="Project thumbnails placed in the diamond frames" style="left:0;top:0;width:0;height:0"></span>

      <span class="project-label" style="left:44px;top:107px">Project Name</span>
      <span class="project-label" style="left:44px;top:173px">Project Name</span>
      <span class="project-label" style="left:44px;top:238px">Project Name</span>
      <span class="project-label" style="left:44px;top:308px">Project Name</span>
      <span class="project-label" style="left:481px;top:108px">Project Name</span>
      <span class="project-label" style="left:481px;top:174px">Project Name</span>
      <span class="project-label" style="left:481px;top:240px">Project Name</span>
      <span class="project-label" style="left:481px;top:311px">Project Name</span>
      <span class="project-label" style="left:259px;top:363px">Project Name</span>

      <div class="feature-photo" role="img" aria-label="Photo of a completed fit-out interior with ceiling lights"></div>
      <h3 class="feature-name">Project Name</h3>
      <p class="feature-text">We have a few pictures of jobs which we've completed and would like to show off with a brief description</p>
      <div class="dots" style="left:546px;top:191px"><span class="on"></span><span></span><span></span><span></span></div>
    </section>

    <section class="capabilities-peek">
      <h2 class="section-title abs" style="left:0;width:576px;top:28px"><em>Our</em> Capabilities</h2>
      <p class="section-lede abs" style="left:0;width:576px;top:64px">Just a list of what services we offer</p>
    </section>
  </div>

  <!-- right column -->
  <div class="column column-right">
    <section class="capabilities" role="img" aria-label="Dark photo of a warehouse with a boom lift">
      <h2 class="section-title abs" style="left:0;width:623px;top:36px"><em>Our</em> Capabilities</h2>
      <p class="section-lede abs" style="left:0;width:623px;top:73px">Just a list of what services we offer</p>

      <svg class="abs" style="left:0;top:0" width="623" height="408">
        <defs>
          <g id="cap-tile">
            <polygon points="0,-38 38,0 0,38 -38,0" fill="#9a9a9a"/>
            <polygon points="0,-30 30,0 0,30 -30,0" fill="#e21b22"/>
            <circle r="12" fill="none" stroke="#fff" stroke-width="2"/>
            <path d="M2,-8 L-5,1 L0,1 L-2,8 L5,-1 L0,-1 Z" fill="#fff"/>
          </g>
        </defs>
        <use href="#cap-tile" x="86" y="162"/>
        <use href="#cap-tile" x="233" y="162"/>
        <use href="#cap-tile" x="391" y="162"/>
        <use href="#cap-tile" x="535" y="162"/>
        <use href="#cap-tile" x="154" y="270"/>
        <use href="#cap-tile" x="307" y="270"/>
        <use href="#cap-tile" x="469" y="270"/>
        <rect x="303" y="364" width="14" height="23" rx="7" fill="none" stroke="#ddd" stroke-width="1.3"/>
        <line x1="310" y1="369" x2="310" y2="375" stroke="#ddd" stroke-width="1.3"/>
      </svg>

      <span class="cap-label" style="left:24px;top:207px">Lorem Ipsum</span>
      <span class="cap-label" style="left:169px;top:207px">Lorem Ipsum</span>
      <span class="cap-label" style="left:327px;top:207px">Lorem Ipsum</span>
      <span class="cap-label" style="left:480px;top:207px">Lorem Ipsum</span>
      <span class="cap-label" style="left:93px;top:316px">Lorem Ipsum</span>
      <span class="cap-label" style="left:244px;top:316px">Lorem Ipsum</span>
      <span class="cap-label" style="left:407px;top:316px">Lorem Ipsum</span>

      <div class="dots" style="left:591px;top:186px"><span></span><span></span><span class="on"></span><span></span><span></span></div>
    </section>

    <section class="contact">
      <div class="world-map" role="img" aria-label="Faint dotted world map"></div>
      <h2 class="section-title abs" style="left:0;width:623px;top:30px;font-size:25px">Contact Us</h2>
      <p class="section-lede abs" style="left:0;width:623px;top:69px;font-size:8.5px">Get in touch with us today</p>

      <div class="field field-line" style="top:116px">Your Name :</div>
      <div class="field field-line" style="top:164px">Your Phone :</div>
      <div class="field field-line" style="top:211px">Your Email :</div>
      <div class="field field-area" style="top:261px">Your Message :</div>
      <span class="btn-browse">Browse</span>
      <span class="btn-send">SEND</span>

      <div class="dots" style="left:590px;top:170px"><span></span><span></span><span></span><span class="dark"></span></div>
    </section>

    <footer class="site-footer">
      <p class="copyright">Copyright © bramwellelectrical.com. All rights reserved</p>
      <span class="social" style="left:485px"></span>
      <span class="social" style="left:518px"></span>
      <span class="social" style="left:551px"></span>
    </footer>
  </div>

</div>
</body>
</html>
```